Life Coaching and Career Coaching company needs new website with bold, modern, videos

We need a whole new website that is heavy on video. We are a small company who sells personal wellbeing services like career coaching, life coaching, and group coaching programs. The programs all help people design a better life.
FULL BRIEF ATTACHED and STYLE GUIDE
Also, look at https://www.brightfennel.com/coaching and galdrove.com and https://www.marnwick.life/ for a small amount of inspiration.

Industry/Entity Type

personal well-being/life coaching/career coaching

Number of Pages Required

3 page

Other font styles liked:
• fonts are in the brief

Requirements
Must have
• read the brief please - it's all in there. (things like the look, feel, how it will have lots of video, etc,)
Nice to have
• something really different looking and breakthrough. visually stunning. very trustworthy. Please read the brief, its all in there.
Should not have
• should not look like other life coaching websites. must have video!

```html
<!DOCTYPE html>
<html lang="en">
<head>
<meta charset="utf-8">
<title>Brightpath Design Project — Career &amp; Life Coaching</title>
<link rel="stylesheet" href="https://fonts.googleapis.com/css2?family=Baumans&family=Jost:wght@400;500;600&display=swap">
<style>
:root{
  --coral:#ef6a64;
  --coral-soft:#f27b74;
  --plum:#4a0f45;
  --teal:#0c5b5a;
  --teal-deep:#0f4f4e;
  --slate:#35495b;
  --ink:#2a2a2a;
  --grey:#6f6f6f;
  --line:#e2dede;
  --white:#ffffff;
  --star:#e07a1f;
}
*{margin:0;padding:0;box-sizing:border-box}
html,body{width:1200px;height:3771px;overflow:hidden;background:var(--white)}
body{position:relative;font-family:"Jost",sans-serif;color:var(--ink)}
.abs{position:absolute}
.display{font-family:"Baumans",cursive}
.photo{position:absolute;overflow:hidden}
.pill{border-radius:999px}
.btn{position:absolute;display:flex;align-items:center;justify-content:center;border-radius:999px;font-size:13px;font-weight:500}
.btn-plum{background:var(--plum);color:var(--white)}
.btn-outline{border:1.5px solid var(--plum);color:var(--plum);background:var(--white)}
.play{position:absolute;border-radius:50%;background:var(--white);display:flex;align-items:center;justify-content:center;box-shadow:0 4px 14px rgba(0,0,0,.2)}
.play svg{display:block}

/* header */
.site-header{position:absolute;left:0;top:0;width:1200px;height:82px;background:var(--white)}
.brand{position:absolute;font-weight:500;letter-spacing:1px;color:var(--slate)}
.main-nav{position:absolute;left:502px;top:34px;display:flex;font-size:12px;color:var(--ink)}
.main-nav span{padding:0 14px;border-left:1px solid #bbb;line-height:13px}
.main-nav span:first-child{border-left:none;padding-left:0}

/* hero */
.hero{position:absolute;left:0;top:82px;width:1200px;height:616px;background:var(--coral);overflow:hidden}
.hero-welcome{left:151px;top:80px;font-size:11px;letter-spacing:5px;color:#ffd9d5;display:flex;align-items:center;gap:14px}
.hero-welcome i{display:block;width:140px;height:1px;background:#f9a9a3}
.hero-line{font-size:74px;line-height:1;white-space:nowrap}
.hero-text{font-size:11px;line-height:15px;color:var(--white)}

/* ticker */
.ticker{position:absolute;left:0;top:698px;width:1200px;height:44px;background:var(--slate);color:var(--white);font-size:12px;display:flex;align-items:center;white-space:nowrap;overflow:hidden}
.ticker span{margin:0 10px}
.ticker b{color:var(--coral);font-weight:400}

/* sections */
.section-title{font-size:44px;line-height:48px;color:#5b5b5b}
.body-copy{font-size:11px;line-height:15px;color:var(--ink)}

.programs-band{position:absolute;left:0;top:1494px;width:1200px;height:440px;background:var(--teal)}
.bullets{list-style:none;font-size:11px;line-height:15px;color:var(--white)}
.bullets li{position:relative;padding-left:12px;margin-bottom:8px}
.bullets li:before{content:"";position:absolute;left:0;top:6px;width:4px;height:4px;border-radius:50%;background:var(--white)}

.quote-card{position:absolute;top:2382px;width:275px;height:264px;background:var(--white);border-radius:12px;box-shadow:0 6px 24px rgba(0,0,0,.09);text-align:center}
.quote-card .stars{position:absolute;left:0;right:0;top:116px;color:var(--star);font-size:16px;letter-spacing:2px}
.quote-card p{position:absolute;left:24px;right:24px;top:142px;font-size:11px;line-height:17px;color:var(--ink)}
.author{position:absolute;left:0;right:0;top:218px;display:flex;justify-content:center;align-items:center;gap:6px;text-align:left}
.avatar{width:24px;height:24px;border-radius:50%;background:linear-gradient(135deg,#3a4d72,#c99a7e)}
.author strong{display:block;font-family:"Baumans",cursive;font-weight:400;font-size:14px;color:#555;line-height:14px}
.author small{display:block;font-size:9px;color:#888}

.accordion{position:absolute;left:585px;top:2944px;width:428px}
.acc-row{display:flex;justify-content:space-between;align-items:flex-start;border-bottom:1px solid var(--line);padding:10px 0 12px}
.acc-row .label{font-family:"Baumans",cursive;font-size:15px;color:var(--ink)}
.acc-row .label em{font-family:"Jost",sans-serif;font-style:italic;font-size:15px;margin-right:14px}
.acc-row .sign{color:#999;font-size:14px;padding-right:10px}
.acc-row .detail{font-size:11px;line-height:16px;color:var(--ink);margin:8px 0 0 34px;width:370px}

.newsletter{position:absolute;left:0;top:3433px;width:1200px;height:94px;background:var(--slate)}
.site-footer{position:absolute;left:0;top:3527px;width:1200px;height:244px;background:var(--coral);color:var(--white)}
.footer-nav{position:absolute;left:224px;top:160px;width:752px;display:flex;justify-content:space-between;font-size:12px}
.footer-nav i{font-style:normal;opacity:.6}
.social{position:absolute;top:199px;width:28px;height:28px;border-radius:50%;background:var(--coral-soft);border:1px solid #f9a29c}
</style>
</head>
<body>

<!-- Header -->
<header class="site-header">
  <div class="brand" style="left:168px;top:26px;font-size:22px;line-height:24px">BRIGHTPATH DESIGN</div>
  <div class="brand" style="left:290px;top:50px;font-size:10px;letter-spacing:1px">PROJECT</div>
  <nav class="main-nav">
    <span>Home</span><span>Mission</span><span>Our Programs</span><span>Testimonials</span><span>Events</span>
  </nav>
  <div class="btn btn-plum" style="left:909px;top:23px;width:123px;height:38px">Contact Us</div>
  <svg class="abs" style="left:1000px;top:58px" width="36" height="12"><path d="M2 10 Q18 8 34 1" stroke="var(--plum)" fill="none" stroke-width="1"/><path d="M8 11 Q22 9 32 5" stroke="var(--plum)" fill="none" stroke-width="1"/></svg>
</header>

<!-- Hero -->
<section class="hero">
  <div class="abs hero-welcome">WELCOME <i></i></div>
  <div class="abs display hero-line" style="left:138px;top:110px;color:var(--white)">Your Future</div>
  <div class="abs display hero-line" style="left:760px;top:110px;color:var(--white)">is Open</div>
  <div class="abs display hero-line" style="left:205px;top:200px;color:var(--teal-deep)">Create</div>
  <svg class="abs" style="left:424px;top:86px" width="340" height="484" aria-hidden="true"><rect x="1" y="1" width="300" height="478" rx="150" fill="none" stroke="var(--plum)" stroke-width="1"/></svg>
  <div class="photo pill" role="img" aria-label="Two young women looking at a laptop together" style="left:442px;top:93px;width:318px;height:476px;background:linear-gradient(160deg,#e9e6e3 0%,#b8b1a7 45%,#5a6a4a 75%,#dcd6cf 100%)"></div>
  <div class="abs display hero-line" style="left:664px;top:200px;color:var(--plum)">Your Plan!</div>
  <p class="abs hero-text" style="left:151px;top:386px;width:205px">The Brightpath Design Project is rooted in deeply personal stories from some coworkers that saw the need to help younger people who were struggling with whether they were on the 'right track' in their careers.</p>
  <div class="btn btn-plum" style="left:154px;top:492px;width:123px;height:38px">Contact Us</div>
  <svg class="abs" style="left:252px;top:526px" width="30" height="12"><path d="M2 10 Q16 8 28 1" stroke="var(--plum)" fill="none"/><path d="M8 11 Q20 9 28 5" stroke="var(--plum)" fill="none"/></svg>
  <p class="abs hero-text" style="left:820px;top:325px;width:236px">Their own experiences showed them that people today often don't even know what their own unique strengths are in this world, or how that complements their own unique distinct set of values.</p>
</section>

<!-- Ticker -->
<div class="ticker">
  <span>Career Coaching</span><b>★</b><span>Career Coaching</span><b>★</b><span>Career Coaching</span><b>★</b><span>Career Coaching</span><b>★</b><span>Career Coaching</span><b>★</b><span>Career Coaching</span><b>★</b><span>Career Coaching</span><b>★</b><span>Career Coaching</span><b>★</b><span>Career Coaching</span><b>★</b><span>Career Coaching</span><b>★</b><span>Career Coaching</span>
</div>

<!-- Mission -->
<section>
  <h2 class="abs display section-title" style="left:168px;top:808px;font-weight:400">Our Brightpath Design<br>Project Mission</h2>
  <p class="abs body-copy" style="left:168px;top:928px;width:455px">To develop people's skills and confidence through transformational coaching and mentoring so they can live a more fulfilled life by design, achieving the success they desire.</p>
  <p class="abs body-copy" style="left:168px;top:988px;width:440px">What they learned is that those unique strengths and values can be combined with a person's talents, education, and economic desires, which can be all be shaped and crafted into a life plan or "designed path" that creates deep fulfillment beyond normal everyday expectations.</p>
  <div class="photo" role="img" aria-label="Three friends in knit sweaters smiling at a tablet" style="left:168px;top:1127px;width:501px;height:260px;border-radius:30px;background:linear-gradient(120deg,#6f8a3c 0%,#c98a2e 35%,#e2b27a 55%,#8a5a34 80%,#5a6b3a 100%)"></div>
  <svg class="abs" style="left:700px;top:800px" width="360" height="600" aria-hidden="true">
    <rect x="10" y="2" width="336" height="588" rx="168" fill="none" stroke="#f0b0ad" stroke-width="1.2"/>
    <path d="M6 100 Q18 60 48 30" stroke="var(--coral)" fill="none"/><path d="M14 104 Q26 66 52 40" stroke="var(--coral)" fill="none"/>
  </svg>
  <div class="photo pill" role="img" aria-label="Group of smiling students gathered around a laptop" style="left:704px;top:815px;width:326px;height:574px;background:linear-gradient(170deg,#7a5048 0%,#a47d62 30%,#d6b49a 55%,#5a6f82 80%,#a9b3bd 100%)">
    <div class="play" style="left:122px;top:245px;width:82px;height:82px"><svg width="26" height="28"><path d="M2 1 L25 14 L2 27Z" fill="var(--coral)"/></svg></div>
  </div>
</section>

<!-- Programs band -->
<section class="programs-band">
  <h2 class="abs display" style="left:168px;top:68px;font-size:44px;line-height:48px;color:var(--white);font-weight:400">Explaining Our<br>Four Programs</h2>
  <ul class="abs bullets" style="left:620px;top:64px;width:415px">
    <li>Is to make people FEEL that we can help them.</li>
    <li>To make people feel we are different thana other coaching.</li>
    <li>To make people feel we are very trust-worthy, very reputable, and very high quality.</li>
    <li>To make people feel that without us, they will not be able to improve their lives as much as they could if we help them. If they work with us, they will have success and live a better life!!!</li>
  </ul>
</section>
<svg class="abs" style="left:164px;top:1730px" width="50" height="30" aria-hidden="true"><path d="M2 26 Q20 8 44 2" stroke="#f0a09b" fill="none"/><path d="M8 28 Q24 12 46 8" stroke="#f0a09b" fill="none"/></svg>
<div class="photo" role="img" aria-label="Young man and woman studying at a table" style="left:0;top:1749px;width:152px;height:313px;border-radius:0 24px 24px 0;background:linear-gradient(150deg,#d9d4cc,#8d6e5a 50%,#3e4f6e)"></div>
<div class="photo" role="img" aria-label="Two women working together at a desk in a bright office" style="left:168px;top:1749px;width:510px;height:313px;border-radius:24px;background:linear-gradient(130deg,#ebe8e2 0%,#c9c3b8 45%,#7f7a74 75%,#e3dfd9 100%)">
  <div class="play" style="left:215px;top:117px;width:80px;height:80px"><svg width="24" height="26"><path d="M2 1 L23 13 L2 25Z" fill="var(--coral)"/></svg></div>
</div>
<svg class="abs" style="left:650px;top:2036px" width="40" height="34" aria-hidden="true"><path d="M2 30 Q20 22 36 2" stroke="#f0a09b" fill="none"/><path d="M4 34 Q22 26 38 8" stroke="#f0a09b" fill="none"/></svg>
<div class="photo" role="img" aria-label="Four smiling young women standing together" style="left:694px;top:1749px;width:260px;height:313px;border-radius:24px;background:linear-gradient(170deg,#e8ecef,#b9a490 45%,#4d5d7a 80%)"></div>
<div class="photo" role="img" aria-label="Mentor and students gathered around a table with papers" style="left:970px;top:1749px;width:230px;height:313px;border-radius:24px 0 0 24px;background:linear-gradient(160deg,#efe9df,#c9a385 45%,#7d6b78 75%,#c98a4e)"></div>

<!-- Testimonials -->
<section>
  <svg class="abs" style="left:92px;top:2239px" width="140" height="104" aria-hidden="true">
    <path d="M0 0 H58 V60 Q58 98 20 102 L16 86 Q34 80 34 62 H0Z" fill="#e8e8e8"/>
    <path d="M78 0 H136 V60 Q136 98 98 102 L94 86 Q112 80 112 62 H78Z" fill="#e8e8e8"/>
  </svg>
  <h2 class="abs display section-title" style="left:0;width:1200px;top:2164px;text-align:center;font-weight:400">See What People Saying<br>About Us</h2>
  <p class="abs" style="left:0;width:1200px;top:2276px;text-align:center;font-size:11px">Lorem Ipsum is simply dummy text of the printing and typesetting industry.</p>

  <article class="quote-card" style="left:168px">
    <div class="stars">★★★★★</div>
    <p>"Lorem Ipsum is simply dummy text of the printing and typesetting industry lorem Ipsum is simply dummy text of the printing and typesetting."</p>
    <div class="author"><div class="avatar"></div><div><strong>Mara Velt</strong><small>Student</small></div></div>
  </article>
  <article class="quote-card" style="left:462px">
    <div class="stars">★★★★★</div>
    <p>"Lorem Ipsum is simply dummy text of the printing and typesetting industry lorem Ipsum is simply dummy text of the printing and typesetting."</p>
    <div class="author"><div class="avatar"></div><div><strong>Tessa Lorne</strong><small>Student</small></div></div>
  </article>
  <article class="quote-card" style="left:755px">
    <div class="stars">★★★★★</div>
    <p>"Lorem Ipsum is simply dummy text of the printing and typesetting industry lorem Ipsum is simply dummy text of the printing and typesetting."</p>
    <div class="author"><div class="avatar"></div><div><strong>Ravi K Donnel</strong><small>Student</small></div></div>
  </article>

  <div class="photo" role="img" aria-label="Students studying together in a library" style="left:207px;top:2317px;width:197px;height:166px;border-radius:6px;background:linear-gradient(140deg,#5b4a3e,#a27d66 50%,#3e3a3c)">
    <div class="play" style="left:86px;top:71px;width:26px;height:26px;background:transparent;border:2px solid #fff;box-shadow:none"><svg width="8" height="10"><path d="M1 1 L7 5 L1 9Z" fill="#fff"/></svg></div>
  </div>
  <div class="photo" role="img" aria-label="Student holding notebooks in a library aisle" style="left:501px;top:2317px;width:197px;height:166px;border-radius:6px;background:linear-gradient(140deg,#6b5a46,#b79676 50%,#4a5a6a)">
    <div class="play" style="left:86px;top:71px;width:26px;height:26px;background:transparent;border:2px solid #fff;box-shadow:none"><svg width="8" height="10"><path d="M1 1 L7 5 L1 9Z" fill="#fff"/></svg></div>
  </div>
  <div class="photo" role="img" aria-label="Smiling young man with a backpack outdoors" style="left:794px;top:2317px;width:197px;height:166px;border-radius:6px;background:linear-gradient(140deg,#8ca0b8,#a78e7a 50%,#3c5a84)">
    <div class="play" style="left:86px;top:71px;width:26px;height:26px;background:transparent;border:2px solid #fff;box-shadow:none"><svg width="8" height="10"><path d="M1 1 L7 5 L1 9Z" fill="#fff"/></svg></div>
  </div>
</section>

<!-- Programs accordion -->
<section>
  <svg class="abs" style="left:174px;top:2770px" width="346" height="600" aria-hidden="true">
    <rect x="6" y="4" width="334" height="572" rx="167" fill="none" stroke="#f0b0ad" stroke-width="1.2"/>
    <path d="M4 70 Q20 40 44 22" stroke="var(--coral)" fill="none"/><path d="M12 74 Q26 46 50 30" stroke="var(--coral)" fill="none"/>
  </svg>
  <div class="photo pill" role="img" aria-label="Two students looking at a laptop together" style="left:179px;top:2780px;width:319px;height:571px;background:linear-gradient(165deg,#ece8e2 0%,#c2a48a 35%,#6e7f96 60%,#2f2f35 100%)"></div>

  <h2 class="abs display section-title" style="left:585px;top:2806px;font-weight:400">Brightpath Design<br>Project Programs</h2>
  <p class="abs" style="left:587px;top:2917px;font-size:10px">Most popular programs :</p>
  <div class="accordion">
    <div class="acc-row"><span class="label"><em>01</em>On-demand Specialists</span><span class="sign">+</span></div>
    <div class="acc-row" style="display:block"><div style="display:flex;justify-content:space-between"><span class="label"><em>02</em>Dedicated 1:1 Coaching</span><span class="sign">–</span></div>
      <p class="detail">Lorem Ipsum is simply dummy text of the printing and typeset industry lorem Ipsum is simply dummy text of the printing.</p></div>
    <div class="acc-row"><span class="label"><em>03</em>Business Impact Studies</span><span class="sign">+</span></div>
    <div class="acc-row"><span class="label"><em>04</em>People Analytics Dashboard</span><span class="sign">+</span></div>
    <div class="acc-row"><span class="label"><em>05</em>Integrations &amp; Deployment</span><span class="sign">+</span></div>
  </div>
  <div class="btn btn-plum" style="left:585px;top:3241px;width:155px;height:40px">Request A Demo</div>
  <svg class="abs" style="left:712px;top:3278px" width="32" height="12"><path d="M2 10 Q16 8 30 1" stroke="var(--plum)" fill="none"/><path d="M8 11 Q20 9 30 5" stroke="var(--plum)" fill="none"/></svg>
  <div class="btn btn-outline" style="left:749px;top:3241px;width:120px;height:40px">Learn More</div>
</section>

<!-- Newsletter -->
<section class="newsletter">
  <h2 class="abs display" style="left:168px;top:32px;font-size:29px;color:var(--white);font-weight:400">Subscribe Our Newsletter</h2>
  <div class="abs" style="left:622px;top:32px;width:287px;height:37px;border-radius:999px;background:#4a5c6d;color:#8796a5;font-size:11px;display:flex;align-items:center;padding-left:28px">Enter Email Address</div>
  <div class="btn" style="left:918px;top:32px;width:114px;height:37px;background:var(--white);color:var(--slate)">Subscribe</div>
</section>

<!-- Footer -->
<footer class="site-footer">
  <div class="abs" style="left:0;width:1200px;top:86px;text-align:center;font-size:27px;font-weight:500;letter-spacing:1px;line-height:28px">BRIGHTPATH DESIGN</div>
  <div class="abs" style="left:634px;top:115px;font-size:11px;letter-spacing:1px;font-weight:500">PROJECT</div>
  <nav class="footer-nav">
    <span>Home</span><i>|</i><span>Mission</span><i>|</i><span>Our Programs</span><i>|</i><span>Testimonials</span><i>|</i><span>Events</span><i>|</i><span>Contact Us</span>
  </nav>
  <p class="abs" style="left:224px;top:206px;font-size:10px">© Copyright 2024 Brightpath Design Project, LLC</p>
  <span class="social" style="left:551px"></span>
  <span class="social" style="left:586px"></span>
  <span class="social" style="left:621px"></span>
  <p class="abs" style="left:775px;top:206px;font-size:10px">Privacy Policy &nbsp;|&nbsp; Terms &amp; Conditions</p>
</footer>

</body>
</html>
```